Chocolate company needing sticker for products

I have a small chocolate company Brook Lane Sweets in Austin Texas. I make all vegan, gluten free, organic, faire trade chocolate that tastes amazing! It is allergy friendly approvable by all ages. I want to have a great sticker that i can put on our boxes and bags. I am using a lot of natural craft color and brown. I am open to color options possibly for different flavors. I want the packaging to reflect the basis of my company. It is all handmade by me but i don't want it to have to much of a crafty look to it. I have attached the logo designs I have. it the sticker can have som of the bullet points about the company that would be great. But it needs to say Locally Made in Austin Texas. it also has to have the company address.
417 West Harlow Pine Rd #238 Austin Tx 78719. These things are required by the state for food regulations. I want something that looks great and I can be really proud to put on my product! Thanks so much for all of your help in advance. Dee

I also need some other information added to the sticker. Website which is brooklanesweetsqvz.com 

Phone number 512.555.0187. Instagram brooklanesweets. Thanks for your hard work! 

Industry/Entity Type

Chocolate Company

Requirements
Must have
• The logo is added at the bottom as well as designs I like I want to have a professional look but it to be approvable by all consumers. I will gig feed back as i see what designs come through. This will probably fold out into a multi design project so i will be looking for assistance on other areas of this as well. Thanks

```html
<!DOCTYPE html>
<html lang="en">
<head>
<meta charset="utf-8">
<title>Brook Lane Sweets – Chocolate Sticker Options</title>
<link rel="stylesheet" href="https://fonts.googleapis.com/css2?family=Arvo:wght@700&family=Oswald:wght@400;500&family=Roboto+Condensed:wght@500;700&display=swap">
<style>
  :root {
    --cocoa: #3b2210;
    --sky: #bfe0e6;
    --cut-red: #e0242c;
    --paper: #ffffff;
  }
  html, body {
    margin: 0;
    padding: 0;
    overflow: hidden;
    background: var(--paper);
  }
  .canvas {
    display: block;
    width: 1200px;
    height: 1000px;
  }
  .cut-line {
    fill: none;
    stroke: var(--cut-red);
    stroke-width: 1.2;
    stroke-dasharray: 3 3;
  }
  .cut-note {
    fill: var(--cut-red);
    font-family: Arial, Helvetica, sans-serif;
    font-size: 10px;
  }
  .fill-cocoa { fill: var(--cocoa); }
  .fill-sky { fill: var(--sky); }
  .ink-sky { color: var(--sky); }
  .ink-cocoa { color: var(--cocoa); }
  .label-values { font-family: 'Oswald', sans-serif; font-size: 16px; letter-spacing: 0.5px; }
  .label-brand { font-family: 'Oswald', sans-serif; font-weight: 500; font-size: 25px; letter-spacing: 1px; }
  .label-flavour { font-family: 'Arvo', serif; font-weight: 700; font-size: 22px; }
  .label-origin { font-family: 'Roboto Condensed', sans-serif; font-weight: 700; font-size: 9px; }
  .label-brace { font-family: 'Arvo', serif; font-size: 62px; }
  .label-web { font-family: 'Roboto Condensed', sans-serif; font-weight: 500; font-size: 15.5px; }
  .label-contact { font-family: 'Roboto Condensed', sans-serif; font-weight: 700; font-size: 7.4px; }
</style>
</head>
<body>
<svg class="canvas" viewBox="0 0 1200 1000" xmlns="http://www.w3.org/2000/svg">
  <defs>
    <g id="bump"><circle cx="0" cy="-182" r="30"/></g>
    <g id="wavy-badge">
      <circle cx="0" cy="0" r="200"/>
      <use href="#bump" transform="rotate(0)"/>
      <use href="#bump" transform="rotate(22.5)"/>
      <use href="#bump" transform="rotate(45)"/>
      <use href="#bump" transform="rotate(67.5)"/>
      <use href="#bump" transform="rotate(90)"/>
      <use href="#bump" transform="rotate(112.5)"/>
      <use href="#bump" transform="rotate(135)"/>
      <use href="#bump" transform="rotate(157.5)"/>
      <use href="#bump" transform="rotate(180)"/>
      <use href="#bump" transform="rotate(202.5)"/>
      <use href="#bump" transform="rotate(225)"/>
      <use href="#bump" transform="rotate(247.5)"/>
      <use href="#bump" transform="rotate(270)"/>
      <use href="#bump" transform="rotate(292.5)"/>
      <use href="#bump" transform="rotate(315)"/>
      <use href="#bump" transform="rotate(337.5)"/>
    </g>

    <path id="values-arc" d="M -164,-18 A 166 166 0 0 1 164,-18"/>

    <g id="sticker-copy" fill="currentColor">
      <text class="label-values">
        <textPath href="#values-arc" startOffset="50%" text-anchor="middle">VEGAN • GLUTEN FREE • ALLERGY FRIENDLY • ORGANIC • FAIR TRADE</textPath>
      </text>

      <text class="label-brand" text-anchor="middle" x="0" y="-116">BROOK</text>
      <text class="label-brand" text-anchor="middle" x="0" y="-88">LANE</text>
      <text class="label-brand" text-anchor="middle" x="0" y="-60">SWEETS</text>

      <text class="label-brace" text-anchor="middle" x="-148" y="18">{</text>
      <text class="label-brace" text-anchor="middle" x="148" y="18">}</text>

      <text class="label-flavour" text-anchor="middle" x="0" y="5">70% Dark</text>
      <text class="label-flavour" text-anchor="middle" x="0" y="33">Peruvian Chocolate</text>

      <text class="label-origin" text-anchor="middle" x="0" y="58">LOCALLY</text>
      <text class="label-origin" text-anchor="middle" x="0" y="69">MADE IN</text>
      <text class="label-origin" text-anchor="middle" x="0" y="80">AUSTIN</text>
      <text class="label-origin" text-anchor="middle" x="0" y="91">TEXAS</text>

      <text class="label-web" text-anchor="middle" x="0" y="133">WWW.BROOKLANESWEETSQVZ.COM</text>

      <rect x="-58" y="142.6" width="116" height="0.8"/>
      <rect x="-3" y="140" width="6" height="6" transform="rotate(45 0 143)"/>

      <text class="label-contact" text-anchor="middle" x="0" y="158">417 WEST HARLOW PINE RD #238 AUSTIN TX 78719</text>
      <text class="label-contact" text-anchor="middle" x="0" y="168">WWW.SNAPFOLIO.COM/BROOKLANESWEETS</text>
      <text class="label-contact" text-anchor="middle" x="0" y="178">PHONE : 512.555.0187</text>
    </g>
  </defs>

  <!-- Option 1: brown badge, sky outer rim, white margin -->
  <g class="sticker sticker--cocoa-margin" transform="translate(393 271)">
    <circle class="cut-line" r="222"/>
    <use href="#wavy-badge" class="fill-sky"/>
    <use href="#wavy-badge" class="fill-cocoa" transform="scale(0.965)"/>
    <use href="#wavy-badge" class="fill-sky" transform="scale(0.945)"/>
    <use href="#wavy-badge" class="fill-cocoa" transform="scale(0.937)"/>
    <use href="#sticker-copy" class="ink-sky"/>
  </g>
  <text class="cut-note" x="405" y="48" text-anchor="middle">round cut with a white margin all around your sticker</text>

  <!-- Option 2: sky badge, brown outer rim, white margin -->
  <g class="sticker sticker--sky-margin" transform="translate(925 271)">
    <circle class="cut-line" r="222"/>
    <use href="#wavy-badge" class="fill-cocoa"/>
    <use href="#wavy-badge" class="fill-sky" transform="scale(0.965)"/>
    <use href="#wavy-badge" class="fill-cocoa" transform="scale(0.955)"/>
    <use href="#wavy-badge" class="fill-sky" transform="scale(0.945)"/>
    <use href="#sticker-copy" class="ink-cocoa"/>
  </g>
  <text class="cut-note" x="917" y="51" text-anchor="middle">round cut with a white margin all around your sticker</text>

  <!-- Option 3: brown full bleed -->
  <g class="sticker sticker--cocoa-bleed" transform="translate(393 745)">
    <circle class="fill-cocoa" r="222"/>
    <circle class="cut-line" r="222"/>
    <use href="#wavy-badge" class="fill-sky" transform="scale(0.99)"/>
    <use href="#wavy-badge" class="fill-cocoa" transform="scale(0.965)"/>
    <use href="#wavy-badge" class="fill-sky" transform="scale(0.945)"/>
    <use href="#wavy-badge" class="fill-cocoa" transform="scale(0.937)"/>
    <use href="#sticker-copy" class="ink-sky"/>
  </g>
  <text class="cut-note" x="27" y="962">round cut with a bleeding margin all around your sticker</text>
  <text class="cut-note" x="27" y="974">(cut into the brown)</text>

  <!-- Option 4: sky full bleed -->
  <g class="sticker sticker--sky-bleed" transform="translate(925 745)">
    <circle class="fill-sky" r="222"/>
    <circle class="cut-line" r="222"/>
    <use href="#wavy-badge" class="fill-cocoa" transform="scale(0.99)"/>
    <use href="#wavy-badge" class="fill-sky" transform="scale(0.965)"/>
    <use href="#wavy-badge" class="fill-cocoa" transform="scale(0.955)"/>
    <use href="#wavy-badge" class="fill-sky" transform="scale(0.945)"/>
    <use href="#sticker-copy" class="ink-cocoa"/>
  </g>
  <text class="cut-note" x="563" y="962">round cut with a bleeding margin all around your sticker</text>
  <text class="cut-note" x="563" y="974">(cut into the light blue)</text>
</svg>
</body>
</html>
```